Business Card Design - ThriveMetric

Looking for creative, modern design, two sided for ThriveMetric that is consistent with color and feel of website www.thrivemetric.net.

Back of card will be used to promote products or have a quote revolving around decisions, change, leadership, innovation, creativity. Back should also have space to promote website, but optional to use the icon. Front of the card will need to use the icon and have standard place for name, job title, phone and email. We are not looking to put a mailing address or fax. Also want space to place a few words/phrase explaining what we do...such as individual growth and organizational development or tools, training, information...in addition, want the linkpage icon small on the front somewhere as we are also on linkpage.

Vector file uploaded of icon.

Target Market(s)

Professional coaching for individual growth and organizational development

Industry/Entity Type

Business

Requirements
Must have
• Icon...see attached.

```html
<!DOCTYPE html>
<html lang="en">
<head>
<meta charset="utf-8">
<title>ThriveMetric – Business Card</title>
<link rel="stylesheet" href="https://fonts.googleapis.com/css2?family=Exo+2:wght@300;400;700&family=Nunito+Sans:ital,wght@0,400;1,400&display=swap">
<style>
  :root {
    --backdrop: #2a2a2c;
    --card-top: #1f3270;
    --card-bottom: #17285a;
    --accent: #5cc0ec;
    --accent-soft: #7fcff2;
    --text: #ffffff;
    --mark-fill: #9fb4d8;
  }
  * { margin: 0; padding: 0; box-sizing: border-box; }
  html, body { width: 1200px; height: 900px; overflow: hidden; }
  body {
    background: var(--backdrop);
    position: relative;
    font-family: "Exo 2", sans-serif;
    color: var(--text);
  }
  .card {
    position: absolute;
    top: 308px;
    width: 514px;
    height: 284px;
    border-radius: 16px;
    background: linear-gradient(160deg, var(--card-top), var(--card-bottom));
    box-shadow: 0 6px 18px rgba(0,0,0,0.45);
  }
  .card--front { left: 73px; }
  .card--back { left: 616px; }
  .edge-bar {
    position: absolute;
    top: 46px;
    width: 7px;
    height: 176px;
    background: var(--accent);
  }
  .edge-bar--left { left: 0; border-radius: 0 3px 3px 0; }
  .edge-bar--right { right: 0; border-radius: 3px 0 0 3px; }

  /* front */
  .brand-mark {
    position: absolute;
    left: 78px;
    top: 60px;
    width: 112px;
    height: 112px;
    border-radius: 50%;
    background: radial-gradient(circle at 40% 35%, var(--mark-fill), #4f6fa8);
  }
  .brand-name {
    position: absolute;
    left: 42px;
    top: 193px;
    font-size: 27px;
    font-weight: 700;
    color: var(--accent);
    letter-spacing: 0.2px;
  }
  .person {
    position: absolute;
    right: 44px;
    top: 40px;
    text-align: right;
  }
  .person__name { font-size: 20px; font-weight: 300; color: var(--accent); }
  .person__title { font-size: 14px; font-weight: 300; margin-top: 1px; }
  .contact {
    position: absolute;
    right: 44px;
    top: 137px;
    list-style: none;
    text-align: right;
    font-size: 14px;
    font-weight: 300;
  }
  .contact li { display: flex; justify-content: flex-end; align-items: center; gap: 7px; height: 17px; }
  .contact li.contact__social { margin-top: 17px; }
  .contact svg { width: 11px; height: 11px; flex: none; }
  .tagline {
    position: absolute;
    left: 42px;
    top: 250px;
    font-size: 11px;
    font-weight: 400;
    letter-spacing: 0.1px;
    text-transform: uppercase;
  }
  .tagline .sep { color: var(--accent); padding: 0 3px; }

  /* back */
  .quote {
    position: absolute;
    left: 0;
    width: 514px;
    top: 84px;
    text-align: center;
    font-family: "Nunito Sans", sans-serif;
    font-size: 17px;
    line-height: 24px;
  }
  .quote-mark {
    position: absolute;
    font-family: "Exo 2", sans-serif;
    font-weight: 700;
    font-size: 48px;
    line-height: 1;
    color: var(--accent);
  }
  .quote-mark--open { left: 78px; top: 72px; }
  .quote-mark--close { left: 424px; top: 166px; }
  .quote-source {
    position: absolute;
    right: 44px;
    top: 202px;
    font-family: "Nunito Sans", sans-serif;
    font-style: italic;
    font-size: 14px;
    color: var(--accent-soft);
  }
</style>
</head>
<body>

<section class="card card--front">
  <span class="edge-bar edge-bar--left"></span>
  <span class="edge-bar edge-bar--right"></span>

  <span class="brand-mark"></span>
  <div class="brand-name">ThriveMetric</div>

  <div class="person">
    <div class="person__name">Dana Reyes</div>
    <div class="person__title">managing director</div>
  </div>

  <ul class="contact">
    <li>555 010 20 30
      <svg viewBox="0 0 12 12"><circle cx="6" cy="6" r="6" fill="#5cc0ec"/><path d="M4 3.2l1.2 1.6-.6.7c.4.9 1 1.5 1.9 1.9l.7-.6 1.6 1.2-.6 1c-2.4-.2-4.9-2.7-5.1-5.1z" fill="#1b2d62"/></svg>
    </li>
    <li>info@thrivemetric.net
      <svg viewBox="0 0 12 12"><rect x="0.5" y="2.5" width="11" height="7" fill="#5cc0ec"/><path d="M0.5 2.5L6 6.6l5.5-4.1" fill="none" stroke="#1b2d62" stroke-width="1"/></svg>
    </li>
    <li>thrivemetric.net
      <svg viewBox="0 0 12 12"><circle cx="6" cy="6" r="5.3" fill="none" stroke="#5cc0ec" stroke-width="1.2"/><ellipse cx="6" cy="6" rx="2.3" ry="5.3" fill="none" stroke="#5cc0ec" stroke-width="1"/><path d="M0.8 6h10.4" stroke="#5cc0ec" stroke-width="1"/></svg>
    </li>
    <li class="contact__social">linkpage.com/thrivemetric
      <svg viewBox="0 0 12 12"><rect x="0.5" y="0.5" width="11" height="11" rx="1" fill="#5cc0ec"/></svg>
    </li>
  </ul>

  <div class="tagline">Individual Growth<span class="sep">|</span>Organizational Development<span class="sep">|</span>Training<span class="sep">|</span>Information</div>
</section>

<section class="card card--back">
  <span class="edge-bar edge-bar--left"></span>
  <span class="edge-bar edge-bar--right"></span>

  <span class="quote-mark quote-mark--open">&ldquo;</span>
  <blockquote class="quote">
    The significant problems we face<br>
    cannot be solved at the same level<br>
    of thinking we were at when<br>
    we created them.
  </blockquote>
  <span class="quote-mark quote-mark--close">&rdquo;</span>
  <div class="quote-source">– Adrian Whitfield</div>
</section>

</body>
</html>
```